Dentist Ad for Airline Magazine

A full page print ad for magazine. Details below.

Target Market(s)

Mine workers and rural patients who fly in and out of the main city.

Industry/Entity Type

Airline

Requirements
Must have
• Copywriting as per attachment. Magazine print specifications as per attachment. Inviting colours (blue shades, perhaps some green/yellow). Comforting look and picture. Professional feel. Picture can be of a smiling or sleeping relaxed person (see business websites http://www.calmharbourdentalcare.com and http://www.wexmoredentalpractice.com.au) - as we bring patients with complex dental problems or fear of the dentist, back to health whilst they enjoy a relaxing sleep (sedation).
Nice to have
• - stylised image of an aeroplane route across the text or at the footer

```html
<!DOCTYPE html>
<html lang="en">
<head>
<meta charset="utf-8">
<title>Fly-in Fly-out Dental Transformations</title>
<link rel="stylesheet" href="https://fonts.googleapis.com/css2?family=Arimo:wght@400;700&family=Fredoka:wght@500;600&display=swap">
<style>
  :root {
    --blue-top: #1d9ee2;
    --blue-deep: #0b8bd3;
    --blue-light: #4db6ea;
    --blue-text: #1592d6;
    --navy-text: #1b4f86;
    --yellow: #f6ee20;
    --white: #ffffff;
    --green-top: #a6d12c;
    --green-mid: #55a834;
    --green-deep: #20802f;
    --amp: rgba(190, 225, 150, 0.75);
  }
  * { box-sizing: border-box; margin: 0; padding: 0; }
  html, body { width: 1033px; height: 1200px; overflow: hidden; background: #ffffff; }
  .ad {
    position: relative;
    width: 1033px;
    height: 1200px;
    font-family: "Arimo", Arial, sans-serif;
    color: var(--white);
    background: linear-gradient(180deg, var(--blue-top) 0%, var(--blue-deep) 50%);
    overflow: hidden;
  }
  .intro { position: absolute; left: 72px; top: 46px; right: 56px; }
  .headline {
    font-family: "Fredoka", sans-serif;
    font-weight: 600;
    color: var(--yellow);
    font-size: 47px;
    line-height: 1.02;
    letter-spacing: -0.3px;
    text-shadow: 0 2px 6px rgba(0, 40, 90, 0.35);
  }
  .headline .sub { display: block; font-size: 38px; font-weight: 500; margin-top: 4px; }
  .intro p {
    font-weight: 700;
    font-size: 15.4px;
    line-height: 1.36;
    margin-top: 14px;
  }
  .intro p + p { margin-top: 20px; }

  .faces {
    position: absolute;
    left: 72px; top: 340px;
    width: 889px; height: 250px;
    background: var(--white);
    display: flex; gap: 17px;
    padding: 16px 17px;
  }
  .face { flex: 1; height: 100%; }
  .face.f1 { background: linear-gradient(160deg, #8a6b55, #c9a58a 55%, #2d3a5c); }
  .face.f2 { background: linear-gradient(160deg, #c8d3de, #d7b59e 55%, #6f8fa8); }
  .face.f3 { background: linear-gradient(160deg, #5a3a2c, #e2c2ab 55%, #b58d73); }
  .face.f4 { background: linear-gradient(160deg, #e6e6e6, #d8ae8e 55%, #a98063); }

  .why-title {
    position: absolute; left: 72px; top: 606px;
    font-weight: 700; font-size: 55px; letter-spacing: -0.5px;
    line-height: 1;
  }
  .why {
    position: absolute; left: 0; top: 650px; width: 100%; height: 177px;
    background: var(--white);
    display: flex; gap: 23px;
    padding: 14px 56px 0 72px;
  }
  .why p {
    flex: 1;
    font-size: 15.4px; line-height: 1.34;
    color: var(--navy-text);
  }
  .why .lead { color: var(--blue-text); }
  .why strong { color: var(--navy-text); }

  .proof {
    position: absolute; left: 0; top: 827px; width: 100%; height: 176px;
    background: linear-gradient(180deg, var(--blue-deep) 0%, var(--blue-light) 100%);
    padding: 28px 56px 0 72px;
  }
  .proof h2 {
    font-family: "Fredoka", sans-serif; font-weight: 500;
    font-size: 33px; line-height: 1.12;
  }
  .proof p { font-size: 14.6px; line-height: 1.4; margin-top: 14px; }

  .contact {
    position: absolute; left: 0; top: 1003px; width: 100%; height: 197px;
    background: linear-gradient(180deg, var(--green-top) 0%, var(--green-mid) 55%, var(--green-deep) 100%);
    text-align: center;
  }
  .call {
    padding-top: 14px;
    font-family: "Fredoka", sans-serif; font-weight: 600;
    color: var(--yellow); font-size: 26px;
    text-shadow: 0 1px 4px rgba(20, 70, 20, 0.35);
  }
  .call .phone { font-size: 36px; }
  .address { color: var(--yellow); font-weight: 700; font-size: 14px; margin-top: 2px; }
  .practice {
    position: absolute; top: 80px; width: 320px; text-align: left;
  }
  .practice.left { left: 128px; }
  .practice.right { left: 620px; }
  .brand {
    display: flex; align-items: center; gap: 12px;
    font-weight: 700; font-size: 24px; color: var(--white);
    height: 54px;
  }
  .brand-mark { width: 34px; height: 34px; flex: none; }
  .practice .lines {
    margin-top: 6px; margin-left: 46px;
    font-weight: 700; font-size: 14.6px; line-height: 1.3; text-align: center; display: inline-block;
  }
  .practice.right .lines { margin-left: 0; text-align: left; }
  .amp {
    position: absolute; left: 491px; top: 88px;
    font-family: "Arimo", sans-serif; font-weight: 700; font-size: 78px; color: var(--amp);
  }
</style>
</head>
<body>
<main class="ad">
  <section class="intro">
    <h1 class="headline">Fly-in Fly-out Dental Transformations
      <span class="sub">True Care, Advanced Expertise, Minimal Visits</span></h1>
    <p>Are you embarrassed to smile? Do you have complex dental problems and don't know where to start?<br>
    Do you suffer from fear of the dentist or just can't find the right one? No time for endless appointments?<br>
    Do you wish you could just sleep your way to a healthy and attractive smile?</p>
    <p>If the answer is yes to any of these questions, you are certainly not alone! In our specialized Sleep Dentistry Centre, our renowned team provides gentle, compassionate, advanced and extensive treatments often in the comfort of a relaxing sleep (IV Sedation).</p>
  </section>

  <div class="faces">
    <div class="face f1" role="img" aria-label="Portrait of a smiling young woman with long brown hair"></div>
    <div class="face f2" role="img" aria-label="Portrait of a smiling older man with grey hair"></div>
    <div class="face f3" role="img" aria-label="Portrait of a smiling woman resting her hand on her cheek"></div>
    <div class="face f4" role="img" aria-label="Portrait of a smiling young man"></div>
  </div>

  <h2 class="why-title">WHY US?</h2>
  <section class="why">
    <p><span class="lead">We take the time to understand your needs</span> so you can make the best decisions for your health. You are looked after by a friendly, highly qualified expert team in relaxed and comfortable surroundings.</p>
    <p><span class="lead">Our unique, time-saving approach</span> means our patients often have advanced treatments that would normally take months in minimal visits - perfect for the Fly-in, Fly-out patient.</p>
    <p><span class="lead">We offer a full range of dental treatments</span> including dental implant surgeries and cosmetic rehabilitations all in-house.</p>
    <p><span class="lead">Our approach with Sleep Dentistry means Pain-Free, anxiety free, memory free procedures.</span> <strong>Just excellent results and life changing treatments.</strong></p>
  </section>

  <section class="proof">
    <h2>Sound too good to be true?<br>It's just what we do for our patients every day.</h2>
    <p>Our patients come from all over Western Australia to take advantage of this unique and personalized service.<br>
    We invite you to let us care for you as well.</p>
  </section>

  <footer class="contact">
    <div class="call">Call our friendly team today &bull; <span class="phone">(08) 9460 2715</span></div>
    <div class="address">42 Harbour Lane Westbrook WA 6010</div>

    <div class="practice left">
      <div class="brand">
        <svg class="brand-mark" viewBox="0 0 34 34" aria-hidden="true"><circle cx="17" cy="17" r="15" fill="#1b4f86"/></svg>
        Calm Harbour Dental Care
      </div>
      <div class="lines">www.calmharbourdentalcare.com<br>info@calmharbourdentalcare.com<br>9460 2714</div>
    </div>

    <div class="amp" aria-hidden="true">&amp;</div>

    <div class="practice right">
      <div class="brand">
        <svg class="brand-mark" viewBox="0 0 34 34" aria-hidden="true"><rect x="3" y="3" width="28" height="28" fill="#ffffff"/></svg>
        wexmore dental
      </div>
      <div class="lines">www.wexmoredentalpractice.com.au<br>info@wexmoredentalpractice.com.au<br>9460 2715</div>
    </div>
  </footer>
</main>
</body>
</html>
```